We need to redesign the app icon and splash screen for our app called "Rotation Ledger". The app records the amount of bench-time and game-time for each player in a team. The target of the app is a quantitative measure of the participation in the game by the players in a team. The app is available on Appvault.

The app can be used by coaches to make sure all players get an equal amount of game-time and by parents to make sure their children get a fair go.

The app is a universal iOS app (iPhone 4,5 and iPad) so the splash screen needs to suit multiple resolutions in both portrait and landscape.

Thank you all for submitting designs. They are all very good and it is quite hard to decide amongst your good designs.

We are going through them all this afternoon and we will select the design we will move forward with.

Once again thank you

regards

Colin Feeney

Target Market(s)

Parents of children at school, teachers, coaches, team managers

Industry/Entity Type

Landscape

Requirements
Must have
• app icon 1024x1024

Splash Screens in both portrait and landscape a version for each of these resolutions (the splash screen must have two buttons (Get Started and Introduction)

iPhone
320x480, 640x960, 640x1136

iPad
1536x2048, 768x1024

```html
<!DOCTYPE html>
<html lang="en">
<head>
<meta charset="utf-8">
<title>Rotation Ledger – Splash</title>
<link rel="stylesheet" href="https://fonts.googleapis.com/css2?family=Alfa+Slab+One&family=Alegreya+Sans:wght@400&display=swap">
<style>
  :root {
    --sky-top: #9fd0ee;
    --sky-bottom: #eef8fc;
    --field-light: #8fcf55;
    --field-dark: #3e9a2e;
    --title-red: #b3181d;
    --title-black: #161616;
    --glow: #ffffff;
    --ink: #111111;
    --step-green: #2b7a2f;
    --step-red: #9e1219;
    --button-top: #4fc0f4;
    --button-mid: #1f74d6;
    --button-bottom: #173f9c;
    --button-edge: #0b1633;
    --figure-tone: rgba(235, 238, 242, 0.85);
  }
  * { margin: 0; padding: 0; box-sizing: border-box; }
  html, body { width: 800px; height: 1200px; overflow: hidden; }
  body {
    position: relative;
    background: linear-gradient(180deg, var(--sky-top) 0%, var(--sky-bottom) 72%);
    font-family: "Alegreya Sans", sans-serif;
  }
  .field-scene {
    position: absolute; left: 0; top: 0; width: 800px; height: 1200px;
  }
  .referee-illustration {
    position: absolute; left: 0; top: 300px; width: 440px; height: 900px;
    background: radial-gradient(ellipse 60% 55% at 35% 45%, var(--figure-tone) 0%, rgba(235,238,242,0.45) 55%, rgba(235,238,242,0) 100%);
  }
  .title {
    position: absolute; left: 0; right: 0; text-align: center;
    font-family: "Alfa Slab One", serif; font-weight: 400; line-height: 1;
    text-shadow: 0 0 4px var(--glow), 0 0 8px var(--glow), 0 0 14px var(--glow);
  }
  .title-main {
    top: 22px; font-size: 118px; letter-spacing: 8px; color: var(--title-red);
  }
  .title-sub {
    top: 120px; font-size: 100px; letter-spacing: 8px; color: var(--title-black);
  }
  .tagline {
    position: absolute; top: 222px; left: 0; right: 0; text-align: center;
    font-size: 62px; line-height: 70px; color: var(--ink);
  }
  .steps {
    position: absolute; left: 428px; top: 372px;
    list-style: none; font-size: 41px; line-height: 65px; color: var(--ink);
  }
  .steps .on { color: var(--step-green); }
  .steps .off { color: var(--step-red); }
  .action-button {
    position: absolute; left: 106px; width: 597px; height: 154px;
    border: 5px solid var(--button-edge); border-radius: 14px;
    background: linear-gradient(180deg, var(--button-top) 0%, var(--button-mid) 52%, var(--button-bottom) 100%);
    box-shadow: inset 0 3px 0 rgba(255,255,255,0.5), 0 4px 8px rgba(0,0,0,0.35);
    display: flex; align-items: center; justify-content: center;
    font-family: "Alfa Slab One", serif; font-size: 54px; letter-spacing: 4px;
    color: #ffffff;
    text-shadow: -2px -2px 0 var(--button-edge), 2px -2px 0 var(--button-edge), -2px 2px 0 var(--button-edge), 2px 2px 0 var(--button-edge), 4px 4px 0 var(--button-edge);
  }
  .button-intro { top: 741px; }
  .button-start { top: 954px; }
</style>
</head>
<body>
  <svg class="field-scene" viewBox="0 0 800 1200" role="img" aria-label="Sports field with green grass, a rolling hill and white line markings">
    <defs>
      <linearGradient id="grass" x1="0" y1="0" x2="0" y2="1">
        <stop offset="0" stop-color="var(--field-light)"/>
        <stop offset="1" stop-color="var(--field-dark)"/>
      </linearGradient>
    </defs>
    <path d="M0 1000 C 250 985 520 960 800 880 L 800 1200 L 0 1200 Z" fill="url(#grass)"/>
    <path d="M0 1070 L 800 1040" stroke="#ffffff" stroke-width="12" opacity="0.8"/>
  </svg>
  <div class="referee-illustration" role="img" aria-label="Cartoon referee in striped shirt and cap holding up a stopwatch"></div>

  <h1 class="title title-main">ROTATION</h1>
  <h2 class="title title-sub">LEDGER</h2>
  <p class="tagline">Record each players game time</p>

  <ol class="steps">
    <li>It's this easy...</li>
    <li>1. Enter players name.</li>
    <li>2. <span class="on">Tap to go on.</span></li>
    <li>3. <span class="off">Tap to go off.</span></li>
  </ol>

  <div class="action-button button-intro">INTRODUCTION</div>
  <div class="action-button button-start">GET STARTED</div>
</body>
</html>
```